Business Card design for an International Import Export House

We need a Business Card design for our import export business. We trade in Minerals, Metals, Rice, Sugar, Steel etc.. The design should be minimalistic. It may or may not contain the physical address. In case you want to include the physical address - 418 Verandah Heights, Marlow Sector 9, Noravi, Rajasthan, India, 302418.

Target Market(s)

Steel Mills or Steel Plants, Factories, Mining businesses, Industrial houses, Government Agencies

Industry/Entity Type

Importer

Contact Information for Business Card

Business Name - Tessan Overseas

Font styles to use
Other font styles liked:
• montserrat

Requirements
Must have
• Ravi Kandola - President
• www.tessanoverseas.com
• ravi@tessanoverseas.com
• +91-987-654-3217
Nice to have
• worldwide suppliers of ores

```html
<!DOCTYPE html>
<html lang="en">
<head>
<meta charset="utf-8">
<title>Tessan Overseas – Business Card</title>
<link rel="stylesheet" href="https://fonts.googleapis.com/css2?family=Montserrat:wght@400;500;600&display=swap">
<style>
  :root {
    --stage: #3b3b3b;
    --card: #ffffff;
    --teal: #4596ad;
    --teal-deep: #3f889f;
    --teal-soft: #7fb8c9;
    --ink: #1d1d1d;
  }
  * { margin: 0; padding: 0; box-sizing: border-box; }
  html, body { width: 1200px; height: 900px; overflow: hidden; }
  body {
    background: var(--stage);
    font-family: "Montserrat", Arial, sans-serif;
    position: relative;
  }
  .card {
    position: absolute;
    top: 192px;
    width: 298px;
    height: 515px;
    background: var(--card);
    overflow: hidden;
  }
  .card--front { left: 288px; }
  .card--back  { left: 614px; }

  /* Front */
  .front-brand {
    position: absolute;
    top: 60px;
    right: 25px;
    text-align: right;
  }
  .wordmark {
    font-weight: 600;
    font-size: 17px;
    letter-spacing: -0.2px;
    color: var(--teal);
    text-transform: uppercase;
    white-space: nowrap;
  }
  .tagline {
    margin-top: 8px;
    font-size: 10.5px;
    line-height: 15px;
    color: var(--teal);
  }
  .front-decoration {
    position: absolute;
    left: 0;
    top: 200px;
    width: 298px;
    height: 315px;
    background: linear-gradient(135deg, var(--teal-soft) 0%, var(--teal) 70%, var(--teal-deep) 100%);
  }

  /* Back */
  .brand-mark {
    position: absolute;
    left: 37px;
    top: 62px;
    width: 64px;
    height: 64px;
    border-radius: 50%;
    background: var(--teal);
  }
  .card--back .wordmark {
    position: absolute;
    left: 37px;
    top: 170px;
  }
  .contact {
    position: absolute;
    left: 37px;
    top: 318px;
    font-size: 12.5px;
    line-height: 17px;
    color: var(--ink);
  }
  .contact__name { text-transform: uppercase; }
  .contact__role { color: var(--teal); font-weight: 500; text-transform: uppercase; }
  .contact__lines { margin-top: 15px; }
  .contact__address { margin-top: 15px; font-style: normal; }
  .web-band {
    position: absolute;
    left: 0;
    bottom: 0;
    width: 100%;
    height: 34px;
    background: var(--teal-deep);
    color: #ffffff;
    font-size: 12.5px;
    line-height: 34px;
    padding-left: 37px;
  }
</style>
</head>
<body>
  <section class="card card--front" aria-label="Card front">
    <div class="front-brand">
      <div class="wordmark">Tessan Overseas</div>
      <p class="tagline">worldwide suppliers<br>of ores</p>
    </div>
    <div class="front-decoration" role="img" aria-label="Large brand emblem decoration in teal"></div>
  </section>

  <section class="card card--back" aria-label="Card back">
    <div class="brand-mark" aria-hidden="true"></div>
    <div class="wordmark">Tessan Overseas</div>
    <div class="contact">
      <p class="contact__name">Ravi Kandola</p>
      <p class="contact__role">President</p>
      <p class="contact__lines">+91-987-654-3217<br>ravi@tessanoverseas.com</p>
      <address class="contact__address">418 Verandah Heights<br>Marlow Sector 9, Noravi<br>Rajasthan, India, 302418</address>
    </div>
    <div class="web-band">www.tessanoverseas.com</div>
  </section>
</body>
</html>
```